Bright Acorn day Nursery flyer

I need a great flyer to attract new parents. Bright Acorn Is a fantastic, warm and homely nursery in Westmere road SE6 London. We offer many things that other nurseries don't offer such as Spanish, Yoga, Music, Cooking classes and Makaton. We also have an amazing system called KINDTRAK that allows parents to get alerts on the KINDTRAK app about their children daily activities and even developmental reports. Parents are able to share with the nursery great moments and put pictures and videos through the app. We also offer the parent camera, an extremely safe system that allows parents to log in and see their children whilst they are engaged in exciting activities.
Full details of Nursery
87 Westmere road
SE6 4QP
02084417260
www.brightacornhollis.co.uk
facebook page
brightacorndaynursery@brightacornhollis.co.uk
Updates

double sided or mini brochure type

Hi Please keep it simple and clean I feel the designs are a good attempt thank you but they are very busy and I just want to add important points a lot of the designs have too many colours, too much text etc Thank you!

https://www.facebook.com/brightacornhollis.co.uk/

Target Market(s)

parents of children 0-5

Industry/Entity Type

Childcare

Colors

Designer to choose colors to be used in the design.

Requirements
Must have
• colour and pictures but clean design

```html
<!DOCTYPE html>
<html lang="en">
<head>
<meta charset="utf-8">
<title>Bright Acorn day Nursery flyer</title>
<link href="https://fonts.googleapis.com/css2?family=Montserrat:wght@500;600;700;800;900&family=Baloo+2:wght@700;800&display=swap" rel="stylesheet">
<style>
:root{
  --blue:#1aa3e0;
  --blue-dark:#0b7fc1;
  --pink:#e4197b;
  --magenta:#c7166f;
  --green:#8cc63f;
  --purple:#8e44ad;
  --orange:#f7941d;
  --yellow:#ffd400;
  --ink:#3a3a3a;
  --white:#ffffff;
}
*{margin:0;padding:0;box-sizing:border-box}
html,body{width:867px;height:1200px;overflow:hidden;background:var(--white)}
.flyer{position:relative;width:867px;height:1200px;overflow:hidden;font-family:"Montserrat",sans-serif;color:var(--ink);background:var(--white)}
.geo-backdrop{position:absolute;left:0;top:0;width:867px;height:560px}
.photo{position:absolute;border:8px solid var(--white);box-shadow:0 4px 12px rgba(0,0,0,.25)}
.photo-painting{left:30px;top:92px;width:320px;height:285px;transform:rotate(-3deg);background:linear-gradient(135deg,#f3d9b8,#e8b98c 50%,#c9d9e8)}
.photo-blocks{left:362px;top:398px;width:312px;height:252px;transform:rotate(2deg);background:linear-gradient(135deg,#f2c7b0,#e27b6a 50%,#f6e2a8)}
.photo-boy{left:515px;top:680px;width:318px;height:288px;background:linear-gradient(135deg,#cfe3f0,#f1c8a8 50%,#7a9cc4)}
.headline{position:absolute;left:445px;top:118px;width:400px;text-align:right;color:var(--white);font-weight:900;font-size:58px;line-height:1.02;letter-spacing:1px;text-shadow:0 3px 6px rgba(0,0,0,.25)}
.values{position:absolute;right:28px;top:322px;list-style:none;text-align:right;font-family:"Baloo 2",sans-serif;font-weight:800;font-size:38px;line-height:1.02;
  text-shadow:0 0 3px #fff,0 0 3px #fff,2px 2px 0 #fff,-2px -2px 0 #fff,2px -2px 0 #fff,-2px 2px 0 #fff,0 2px 0 #fff,0 -2px 0 #fff,2px 0 0 #fff,-2px 0 0 #fff}
.values .learn{color:var(--blue)}
.values .laugh{color:var(--pink)}
.values .grow{color:var(--green)}
.values .share{color:var(--purple)}
.values .happy{color:var(--orange)}
.now-open{position:absolute;left:712px;top:530px;width:138px;height:138px;border-radius:50%;background:var(--blue);border:5px solid var(--white);box-shadow:0 3px 8px rgba(0,0,0,.25);color:var(--white);font-weight:900;font-size:28px;line-height:1.05;display:flex;align-items:center;justify-content:center;text-align:center}
.brand{position:absolute;left:50px;top:560px;width:280px;text-align:center}
.brand-mark{width:110px;height:110px;border-radius:50%;background:var(--pink);margin:0 auto 16px}
.brand-name{font-weight:800;font-size:38px;color:var(--pink);line-height:1.1}
.why{position:absolute;left:45px;top:770px;width:460px}
.why h2{color:var(--pink);font-weight:900;font-size:32px;letter-spacing:.5px;margin-bottom:12px}
.why ul{list-style:none}
.why li{display:flex;align-items:center;gap:10px;font-weight:800;font-size:18px;line-height:1.5;color:var(--ink)}
.why li svg{flex:none}
.hours{position:absolute;left:0;top:992px;width:480px;height:44px;background:var(--pink);color:var(--white);font-weight:800;font-size:17px;display:flex;align-items:center;padding-left:45px;gap:12px;border-radius:0 22px 22px 0;white-space:nowrap}
.hours .time{color:var(--yellow)}
.website{position:absolute;left:520px;top:982px;width:320px;text-align:right;color:var(--pink);font-weight:800;font-size:20px}
.app-note{position:absolute;left:495px;top:1030px;width:345px;height:80px;background:var(--green);border-radius:8px;display:flex;align-items:center;gap:12px;padding:8px 12px;color:var(--white);font-weight:600;font-size:13px;line-height:1.3}
.app-badge{flex:none;width:56px;height:56px;background:var(--white);border-radius:8px}
.phone{position:absolute;left:40px;top:1050px;display:flex;align-items:center;gap:14px}
.phone-icon{width:60px;height:60px;border-radius:50%;background:var(--blue);display:flex;align-items:center;justify-content:center}
.phone-number{color:var(--blue-dark);font-weight:900;font-size:42px;letter-spacing:1px}
.footer{position:absolute;left:0;bottom:0;width:867px;height:76px;background:var(--magenta);color:var(--white);display:flex;justify-content:space-between;align-items:center;padding:0 40px;font-size:15px;font-weight:600;line-height:1.45}
.footer .contact{text-align:left}
</style>
</head>
<body>
<div class="flyer">

  <svg class="geo-backdrop" role="img" aria-label="Colourful low-poly geometric backdrop" viewBox="0 0 867 560" preserveAspectRatio="none">
    <defs>
      <linearGradient id="geo" x1="0" y1="0" x2="1" y2="1">
        <stop offset="0" stop-color="#e4197b"/>
        <stop offset=".3" stop-color="#f7941d"/>
        <stop offset=".55" stop-color="#ffd400"/>
        <stop offset=".75" stop-color="#1aa3e0"/>
        <stop offset="1" stop-color="#8e44ad"/>
      </linearGradient>
    </defs>
    <polygon points="0,0 867,0 867,560 700,420 430,300 0,410" fill="url(#geo)"/>
  </svg>

  <div class="photo photo-painting" role="img" aria-label="Photo of children painting with a nursery teacher"></div>

  <h1 class="headline">LEARNING THROUGH PLAY</h1>

  <ul class="values">
    <li class="learn">Learn</li>
    <li class="laugh">Laugh</li>
    <li class="grow">Grow</li>
    <li class="share">Share</li>
    <li class="happy">Happy</li>
  </ul>

  <div class="photo photo-blocks" role="img" aria-label="Photo of two girls playing with building blocks"></div>

  <div class="now-open">NOW<br>OPEN!</div>

  <div class="brand">
    <div class="brand-mark"></div>
    <div class="brand-name">Bright Acorn</div>
  </div>

  <div class="photo photo-boy" role="img" aria-label="Photo of a young boy playing with a toy"></div>

  <section class="why">
    <h2>WHY CHOOSE US</h2>
    <ul>
      <li><svg width="18" height="18" viewBox="0 0 18 18"><path d="M2 9l5 5 9-11" fill="none" stroke="#e4197b" stroke-width="3" stroke-linecap="round" stroke-linejoin="round"/></svg>WE OFFER UNIQUELY FLEXIBLE HOURS</li>
      <li><svg width="18" height="18" viewBox="0 0 18 18"><path d="M2 9l5 5 9-11" fill="none" stroke="#e4197b" stroke-width="3" stroke-linecap="round" stroke-linejoin="round"/></svg>OUR CONVENIENT LOCATION</li>
      <li><svg width="18" height="18" viewBox="0 0 18 18"><path d="M2 9l5 5 9-11" fill="none" stroke="#e4197b" stroke-width="3" stroke-linecap="round" stroke-linejoin="round"/></svg>FREE PARKING</li>
      <li><svg width="18" height="18" viewBox="0 0 18 18"><path d="M2 9l5 5 9-11" fill="none" stroke="#e4197b" stroke-width="3" stroke-linecap="round" stroke-linejoin="round"/></svg>PLAYROOMS FOR EACH AGE GROUP</li>
      <li><svg width="18" height="18" viewBox="0 0 18 18"><path d="M2 9l5 5 9-11" fill="none" stroke="#e4197b" stroke-width="3" stroke-linecap="round" stroke-linejoin="round"/></svg>ADVENTURE GARDEN</li>
      <li><svg width="18" height="18" viewBox="0 0 18 18"><path d="M2 9l5 5 9-11" fill="none" stroke="#e4197b" stroke-width="3" stroke-linecap="round" stroke-linejoin="round"/></svg>WEB CAMS ARE INSTALLED IN EACH ROOM</li>
    </ul>
  </section>

  <div class="hours"><span>OUR OPENING HOURS</span><span class="time">7.45 AM TO 6.15PM</span></div>

  <div class="website">www.brightacornhollis.co.uk</div>

  <div class="app-note">
    <div class="app-badge"></div>
    <p>We have an amazing system called KINDTRAK that allows parents to get alerts on the KINDTRAK app about their children daily activities</p>
  </div>

  <div class="phone">
    <div class="phone-icon">
      <svg width="30" height="30" viewBox="0 0 24 24"><path d="M6.6 10.8a15.1 15.1 0 006.6 6.6l2.2-2.2c.3-.3.7-.4 1-.2 1.1.4 2.3.6 3.6.6.6 0 1 .4 1 1V20c0 .6-.4 1-1 1A17 17 0 013 4c0-.6.4-1 1-1h3.5c.6 0 1 .4 1 1 0 1.3.2 2.5.6 3.6.1.3 0 .7-.2 1z" fill="#fff"/></svg>
    </div>
    <span class="phone-number">02084417260</span>
  </div>

  <footer class="footer">
    <div class="address">Bright Acorn Day Nursery<br>87 Westmere road London SE6 4QP</div>
    <div class="contact">E: brightacorndaynursery@brightacornhollis.co.uk<br>F: facebook.com/brightacornhollis.co.uk</div>
  </footer>

</div>
</body>
</html>
```